KVT Roofing Pty Ltd

We are a high end residential Roofing company
We would like something silimar to the attached logo with the same color scheme

Target Market(s)

High end residential Builders & Architects

Industry/Entity Type

Residential

```html
<!DOCTYPE html>
<html lang="en">
<head>
<meta charset="utf-8">
<title>KVT Roofing – Business Card</title>
<link rel="stylesheet" href="https://fonts.googleapis.com/css2?family=Roboto:wght@400;500&display=swap">
<style>
  :root {
    --page-bg: #e6e8ea;
    --card-dark: #333c44;
    --card-light: #5a656f;
    --accent-blue: #1ea3dc;
    --text-white: #ffffff;
    --text-soft: #e9edf0;
  }
  * { box-sizing: border-box; margin: 0; padding: 0; }
  html, body {
    width: 1200px;
    height: 1200px;
    overflow: hidden;
    background: var(--page-bg);
    font-family: "Roboto", Arial, sans-serif;
  }
  .canvas {
    position: relative;
    width: 1200px;
    height: 1200px;
  }
  .card {
    position: absolute;
    left: 162px;
    width: 876px;
    height: 500px;
    background: radial-gradient(ellipse at 85% 10%, var(--card-light) 0%, var(--card-dark) 70%);
    box-shadow: 0 10px 30px rgba(0, 0, 0, 0.18);
  }
  .card--front { top: 70px; }
  .card--back { top: 630px; }

  /* Front: brand block */
  .brand-name {
    position: absolute;
    left: 60px;
    top: 210px;
    display: flex;
    align-items: center;
    gap: 16px;
    color: var(--text-white);
    font-weight: 500;
    font-size: 44px;
    letter-spacing: 1px;
  }
  .brand-square {
    width: 26px;
    height: 26px;
    background: var(--accent-blue);
  }

  /* Front: contact block */
  .contact {
    position: absolute;
    left: 390px;
    top: 80px;
    color: var(--text-white);
  }
  .contact-name {
    font-size: 38px;
    font-weight: 400;
    color: var(--text-white);
  }
  .contact-role {
    margin-top: 8px;
    font-size: 30px;
    color: var(--accent-blue);
  }
  .contact-list {
    list-style: none;
    margin-top: 56px;
  }
  .contact-item {
    display: flex;
    align-items: center;
    gap: 18px;
    font-size: 25px;
    color: var(--text-soft);
    height: 62px;
  }
  .contact-icon {
    width: 30px;
    height: 30px;
    flex: none;
  }
  .contact-icon path,
  .contact-icon rect { fill: var(--accent-blue); }

  /* Back: centred brand */
  .back-brand {
    position: absolute;
    inset: 0;
    display: flex;
    align-items: center;
    justify-content: center;
    gap: 26px;
    color: var(--text-white);
    font-weight: 500;
    font-size: 96px;
    letter-spacing: 2px;
  }
  .back-brand .brand-square {
    width: 54px;
    height: 54px;
  }
</style>
</head>
<body>
<main class="canvas">

  <section class="card card--front" aria-label="Business card front">
    <div class="brand-name"><span class="brand-square"></span>KVT Roofing</div>

    <div class="contact">
      <p class="contact-name">Corin Halloway</p>
      <p class="contact-role">General Manager</p>
      <ul class="contact-list">
        <li class="contact-item">
          <svg class="contact-icon" viewBox="0 0 24 24" aria-hidden="true">
            <path d="M12 1.5c-4.3 0-7.5 3.2-7.5 7.3 0 5.4 7.5 13.7 7.5 13.7s7.5-8.3 7.5-13.7c0-4.1-3.2-7.3-7.5-7.3zm0 10.3a3 3 0 1 1 0-6 3 3 0 0 1 0 6z"/>
          </svg>
          218 Fenwick Lane, Harbourvale
        </li>
        <li class="contact-item">
          <svg class="contact-icon" viewBox="0 0 24 24" aria-hidden="true">
            <path d="M6.6 2.5l3 3.4c.5.6.5 1.4 0 2L8.2 9.4c1.3 2.7 3.5 4.9 6.2 6.3l1.5-1.5c.6-.5 1.4-.5 2 0l3.4 3c.6.5.6 1.4.1 2l-1.8 2c-.6.6-1.5.9-2.3.6C10.6 19.6 4.4 13.4 2.2 6.7c-.3-.8 0-1.7.6-2.3l1.8-1.9c.6-.6 1.5-.6 2 0z"/>
          </svg>
          0413 562 908
        </li>
        <li class="contact-item">
          <svg class="contact-icon" viewBox="0 0 24 24" aria-hidden="true">
            <path d="M2 5h20v2.2l-10 6.4L2 7.2z"/>
            <path d="M2 9.6l10 6.4 10-6.4V19H2z"/>
          </svg>
          challoway@kvtroofing.com.au
        </li>
      </ul>
    </div>
  </section>

  <section class="card card--back" aria-label="Business card back">
    <div class="back-brand"><span class="brand-square"></span>KVT Roofing</div>
  </section>

</main>
</body>
</html>
```